Pravel Sales Presentation

We need to create a PowerPoint sales presentation that will convey our company's solutions in an simple manner. In the past we have created presentations using simple bullet form, but haven't found it to be very effective. One suggestion is that we use a combination of some bullets with very simply sketch-type images to help communicate the right message.

We envision receiving a PowerPoint template ready for us to insert our customized content in the format proposed. The design should use our logo and build on it, but doesn't have to follow the exact same style as the logo.

Target Market(s)

Our target market includes large enterprise companies, but also attract mid-sized companies starting at about 10M in revenue. Our solutions are of interest to companies that collect various types of data and want to analyze and use the results for decision making. Examples of customer data include customer purchases, patient health record analysis, social media activity, etc..

Industry/Entity Type

It Company

Requirements
Must have
• -Intro/title page, containing our logo, title of presentation, name of presenter
-Standard sales slides to be used for various purposes, mostly to talk about our offerings
-Slide containing specific content on our GIS solutions. Information about the content can be obtained from this website: http://www.norvanta-example.com/software/location-analytics
-Closing/thank-you slide, containing contact information

Should not have
• Don't want the slides to be overcrowded.

```html
<!DOCTYPE html>
<html lang="en">
<head>
<meta charset="utf-8">
<title>Pravel Slide</title>
<link href="https://fonts.googleapis.com/css2?family=Arimo:wght@400;700&display=swap" rel="stylesheet">
<style>
:root{
  --brand-red:#c8141e;
  --dark-red:#9e0f16;
  --text:#222222;
  --heading:#333333;
  --rule:#d9d9d9;
  --white:#ffffff;
}
*{margin:0;padding:0;box-sizing:border-box}
html,body{width:1200px;height:901px;overflow:hidden;background:var(--white)}
body{font-family:'Arimo',Arial,sans-serif;color:var(--text);position:relative}
.slide{position:absolute;inset:0;width:1200px;height:901px;overflow:hidden;background:var(--white)}
.header{position:absolute;left:0;top:0;width:1200px;height:118px;background:linear-gradient(#ffffff,#f7f7f7);border-bottom:2px solid var(--rule)}
.header-title{position:absolute;left:32px;top:42px;font-size:40px;font-weight:700;color:var(--brand-red);white-space:nowrap}
.brand{position:absolute;right:40px;top:42px;font-size:40px;font-weight:700;color:var(--heading);white-space:nowrap}
.section{position:absolute;left:0;width:1200px}
.section-top{top:120px;height:326px;background:linear-gradient(#ececec,#ffffff 45%)}
.section-bottom{top:446px;height:330px;border-top:1px solid var(--rule);background:linear-gradient(#f0f0f0,#ffffff 40%)}
.section h2{position:absolute;left:32px;font-size:34px;font-weight:700;color:var(--heading);white-space:nowrap}
.section p{position:absolute;left:32px;font-size:25px;line-height:42px;color:var(--text);white-space:nowrap}
.section-top h2{top:62px}
.section-top p{top:128px}
.section-bottom h2{top:52px}
.section-bottom p{top:100px}
.visual{position:absolute}
.visual-screens{left:731px;top:68px;width:465px;height:247px;border-radius:10px;background:linear-gradient(135deg,#3a3d42 0%,#c8cdd3 40%,#e9a06a 70%,#9bb7d4 100%)}
.visual-layers{left:737px;top:64px;width:444px;height:250px;border-radius:8px;background:linear-gradient(#8fc070 0%,#d96a6a 35%,#5b74d6 65%,#d9d9d9 100%)}
.footer{position:absolute;left:0;top:760px;width:1200px;height:141px}
.footer-art{position:absolute;inset:0}
.copyright{position:absolute;left:0;width:1200px;top:838px;text-align:center;font-size:24px;color:#1a1a1a}
.page-badge{position:absolute;left:1102px;top:832px;width:64px;height:64px;border-radius:50%;background:var(--brand-red);border:4px solid var(--white);color:var(--white);font-size:26px;font-weight:700;display:flex;align-items:center;justify-content:center}
</style>
</head>
<body>
<main class="slide">
  <header class="header">
    <h1 class="header-title">Presentation Title here</h1>
    <div class="brand">Pravel</div>
  </header>

  <section class="section section-top">
    <h2>Make New Discoveries</h2>
    <p>Graphs and charts are great, but you can extend your<br>data with location at the helm. Visualize your data on<br>a map to see new patterns. It's easier than you think to<br>enable mapping throughout the enterprise.</p>
    <div class="visual visual-screens" role="img" aria-label="Desktop monitor and laptop displaying map analytics dashboards"></div>
  </section>

  <section class="section section-bottom">
    <h2>Reimagine the Possible</h2>
    <p>You can do much more than simple mapping. Combine<br>your maps with up-to-date demographics, consumer<br>spending, lifestyle, and business data. You can slice,<br>dice, and recombine information to meet any opportu-<br>nity and gain new insight.</p>
    <div class="visual visual-layers" role="img" aria-label="Stacked map layers labelled Demographics, Consumer Lifestyles, Natural Hazards and Your Data"></div>
  </section>

  <div class="footer">
    <svg class="footer-art" width="1200" height="141" viewBox="0 0 1200 141">
      <defs>
        <linearGradient id="globeTone" x1="0" y1="0" x2="1" y2="1">
          <stop offset="0" stop-color="#c9b8c4"/>
          <stop offset="0.5" stop-color="#d9d2d0"/>
          <stop offset="1" stop-color="#b7a9c0"/>
        </linearGradient>
      </defs>
      <path d="M0 141 L0 100 Q600 -60 1200 100 L1200 141 Z" fill="url(#globeTone)" role="img" aria-label="Faint world globe texture"/>
      <path d="M0 100 Q600 -60 1200 100" fill="none" stroke="#9e0f16" stroke-width="5"/>
    </svg>
  </div>
  <div class="copyright">Copyright text here</div>
  <div class="page-badge">01</div>
</main>
</body>
</html>
```